Modern Label for cleaning products for the brand Dorvalix

We need a label design for our line of cleaning products. The label should feature our logo and an image to identify the product's intended use. I've added our logo and an image for use. This only concerns the design of the label on the front of the bottle.

Label dimensions:
Label 1 (500ml bottle with spray): width 58mm x height 115mm
Label 2: (1L bottle): width 73mm x height 140mm
The design must be consistent for both bottles which you find in the pictures.

The bottles to be labeled are white. See the attachment for a photo of the bottles.

The photo must also appear on the label to identify the product's intended use.

Product information:
Brand: Dorvalix
Product: Sanitary Cleaner

This text must be placed on the label:
"Cleans, descales & freshens. followed with this text: "Ideal for quick and powerful cleaning. A ready-to-use product for everyday use."

- Mention the seperate USP's: Sanitary, Bathroom, Toilet, Wet areas

Appearance: This is a consumer product, but it must have a professional appearance. We would like to see a design that use the color blue from our logo.

Target Market(s)

Consumers who take care of their homes and want to maintain it the correct (professional) way

Font styles to use
Sans Serif

Colors
0054AA
0677BA
7BADD7
CADEEF
E8F1F8

Requirements
Must have
• USP's + use of image and logo + blend in 1 design
Nice to have
• Keep the color of the logo in the design
Should not have
• Comic sans

```html
<!DOCTYPE html>
<html lang="en">
<head>
<meta charset="utf-8">
<title>Dorvalix Sanitary Cleaner – Front Labels</title>
<link rel="stylesheet" href="https://fonts.googleapis.com/css2?family=Montserrat:wght@500;600;700;800&display=swap">
<style>
  :root {
    --blue-deep: #0054AA;
    --blue: #0677BA;
    --blue-mid: #7BADD7;
    --blue-light: #CADEEF;
    --blue-pale: #E8F1F8;
    --ink: #1d1d1f;
    --white: #ffffff;
    --canvas: #f7f7f7;
  }
  * { box-sizing: border-box; margin: 0; padding: 0; }
  html, body {
    width: 1200px;
    height: 994px;
    overflow: hidden;
    background: var(--canvas);
    font-family: "Montserrat", Arial, sans-serif;
  }
  .canvas {
    position: relative;
    width: 1200px;
    height: 994px;
  }
  .label {
    position: absolute;
    width: 21em;
    background: var(--white);
    display: flex;
    flex-direction: column;
    align-items: center;
    box-shadow: 0 0.2em 1.2em rgba(0, 0, 0, 0.08);
  }
  .label--spray { left: 203px; top: 375px; font-size: 10px; height: 41.3em; }
  .label--litre { left: 665px; top: 296px; font-size: 12px; height: 41em; }

  .brand {
    display: flex;
    flex-direction: column;
    align-items: center;
    padding-top: 0.8em;
  }
  .brand__dot {
    width: 5em;
    height: 5em;
    border-radius: 50%;
    background: var(--blue);
  }
  .brand__name {
    margin-top: 0.5em;
    font-size: 2.15em;
    font-weight: 700;
    color: var(--ink);
    letter-spacing: -0.01em;
    line-height: 1;
    text-transform: lowercase;
  }
  .product-title {
    margin-top: 0.45em;
    font-size: 1.8em;
    font-weight: 800;
    color: var(--blue);
    text-align: center;
    line-height: 1.05;
    letter-spacing: 0.02em;
  }
  .usage-photo {
    margin-top: 0.5em;
    width: 19.4em;
    flex: 1;
    background: linear-gradient(90deg, #8f8f8c 0%, #b5b4b0 30%, #e7e7e5 55%, #f3f3f3 75%, #cfcfcc 100%);
  }
  .info-band {
    width: 19.4em;
    margin-bottom: 0.9em;
    background: var(--blue);
    color: var(--white);
    text-align: center;
    padding: 0.9em 0.6em 0.7em;
  }
  .info-band__claims {
    font-size: 0.95em;
    font-weight: 600;
    line-height: 1.4;
  }
  .usp-list {
    display: flex;
    align-items: center;
    justify-content: space-between;
    margin-top: 1.2em;
    font-size: 0.72em;
    font-weight: 500;
  }
  .usp-list__items { list-style: none; display: flex; gap: 0.35em; }
  .usp-list__items li + li::before { content: "•"; margin-right: 0.35em; }
  .usp-icon { width: 1.9em; height: 1.9em; display: block; }
</style>
</head>
<body>
<main class="canvas">

  <section class="label label--spray" aria-label="Dorvalix Sanitary Cleaner 500 ml spray label">
    <div class="brand">
      <span class="brand__dot"></span>
      <span class="brand__name">Dorvalix</span>
    </div>
    <h1 class="product-title">SANITARY<br>CLEANER</h1>
    <div class="usage-photo" role="img" aria-label="Photo of a modern bathroom with glass shower, white vanity and pebble-tiled bath"></div>
    <div class="info-band">
      <p class="info-band__claims">Cleans, descales &amp; freshens.<br>Ideal for quick and powerful cleaning.<br>A ready-to-use product for everyday use.</p>
      <div class="usp-list">
        <svg class="usp-icon" viewBox="0 0 20 20" aria-hidden="true"><circle cx="10" cy="10" r="8.5" fill="none" stroke="#fff" stroke-width="1"/><path d="M7 6h6v3a3 3 0 0 1-6 0z M9 12v3h2v-3" fill="none" stroke="#fff" stroke-width="1"/></svg>
        <ul class="usp-list__items"><li>Sanitary</li><li>Bathroom</li><li>Toilet</li><li>Wet Areas</li></ul>
        <svg class="usp-icon" viewBox="0 0 20 20" aria-hidden="true"><circle cx="10" cy="10" r="8.5" fill="none" stroke="#fff" stroke-width="1"/><path d="M10 5c-2 3-3 4.5-3 6a3 3 0 0 0 6 0c0-1.5-1-3-3-6z" fill="none" stroke="#fff" stroke-width="1"/></svg>
      </div>
    </div>
  </section>

  <section class="label label--litre" aria-label="Dorvalix Sanitary Cleaner 1 litre label">
    <div class="brand">
      <span class="brand__dot"></span>
      <span class="brand__name">Dorvalix</span>
    </div>
    <h2 class="product-title">SANITARY<br>CLEANER</h2>
    <div class="usage-photo" role="img" aria-label="Photo of a modern bathroom with glass shower, white vanity and pebble-tiled bath"></div>
    <div class="info-band">
      <p class="info-band__claims">Cleans, descales &amp; freshens.<br>Ideal for quick and powerful cleaning.<br>A ready-to-use product for everyday use.</p>
      <div class="usp-list">
        <svg class="usp-icon" viewBox="0 0 20 20" aria-hidden="true"><circle cx="10" cy="10" r="8.5" fill="none" stroke="#fff" stroke-width="1"/><path d="M7 6h6v3a3 3 0 0 1-6 0z M9 12v3h2v-3" fill="none" stroke="#fff" stroke-width="1"/></svg>
        <ul class="usp-list__items"><li>Sanitary</li><li>Bathroom</li><li>Toilet</li><li>Wet Areas</li></ul>
        <svg class="usp-icon" viewBox="0 0 20 20" aria-hidden="true"><circle cx="10" cy="10" r="8.5" fill="none" stroke="#fff" stroke-width="1"/><path d="M10 5c-2 3-3 4.5-3 6a3 3 0 0 0 6 0c0-1.5-1-3-3-6z" fill="none" stroke="#fff" stroke-width="1"/></svg>
      </div>
    </div>
  </section>

</main>
</body>
</html>
```